We Need a Letterhead + Fax Cover Sheet for Heron Staffing

LETTERHEAD:
- Simple letterhead. Please provide an editable .doc file apart from usual Source Files. Logo Files attached for your use.
- Please place our logo on the upper right corner of the page. You may add some sort of graphic, or light colored background (depends on what looks good).
- Footer should include:
Heron Staffing, LLC
412 Kestrel Ave. Suite 118
Mobile, AL 36619

FAX COVER SHEET:
- Have the logo placed here, should be large, maybe an eight of the page.
- Put:
From:
To:
Phone Number:
Fax Number:

*Still needs some details, will update you because working on the website, etc.

Heron Coastal Workforce Services

```html
<!DOCTYPE html>
<html lang="en">
<head>
<meta charset="UTF-8">
<title>Heron Staffing – Letterhead + Fax Cover Sheet</title>
<link rel="stylesheet" href="https://fonts.googleapis.com/css2?family=Montserrat:wght@400;500&family=Work+Sans:wght@400&family=Lato:wght@400&family=Roboto:wght@400&display=swap">
<style>
  :root {
    --stage: #e0dfe0;
    --paper: #ffffff;
    --brand-blue: #1471ae;
    --brand-olive: #a7b25e;
    --ink: #333333;
    --ink-soft: #555555;
    --ink-dark: #222222;
    --sig-tone: #cfcfcf;
  }
  * { margin: 0; padding: 0; box-sizing: border-box; }
  html, body { width: 1200px; height: 978px; overflow: hidden; }
  body { background: var(--stage); position: relative; font-family: "Lato", sans-serif; }

  .showcase-title {
    position: absolute; top: 92px; left: 0; width: 1200px;
    text-align: center; font-family: "Montserrat", sans-serif; font-weight: 500;
    font-size: 42px; letter-spacing: 1px; color: var(--brand-blue);
  }

  .sheet {
    position: absolute; top: 211px; width: 497px; height: 703px;
    background: var(--paper); box-shadow: 0 3px 10px rgba(0,0,0,0.22);
  }
  .sheet--letter { left: 73px; }
  .sheet--fax { left: 632px; width: 495px; }

  .masthead { position: absolute; top: 27px; left: 0; width: 100%; text-align: center; }
  .masthead__inner { display: inline-block; }
  .masthead__name {
    font-family: "Montserrat", sans-serif; font-weight: 400; font-size: 24px;
    color: var(--brand-blue); letter-spacing: 0.6px; line-height: 1.2;
    padding-bottom: 4px; border-bottom: 1px solid var(--brand-olive);
  }
  .masthead__address {
    font-family: "Work Sans", sans-serif; font-size: 11px; letter-spacing: 0.6px;
    color: var(--ink-soft); margin-top: 6px;
  }

  .letter-body { position: absolute; left: 34px; width: 430px; color: var(--ink); }
  .salutation { top: 234px; font-size: 12px; }
  .paragraph {
    font-family: "Roboto", sans-serif; font-size: 9.6px; line-height: 13px; color: var(--ink-soft);
  }
  .p1 { top: 272px; } .p2 { top: 340px; } .p3 { top: 435px; }
  .closing { top: 514px; font-size: 11.5px; }
  .signer { top: 535px; font-size: 11.5px; line-height: 14px; }
  .signer__role { font-size: 8px; display: block; line-height: 10px; }
  .signature {
    position: absolute; left: 34px; top: 572px; width: 88px; height: 14px;
    background: linear-gradient(90deg, var(--sig-tone), #e8e8e8); border-radius: 7px;
  }

  .brand-mark {
    position: absolute; display: flex; flex-direction: column; align-items: center;
    justify-content: center; text-align: center;
    font-family: "Montserrat", sans-serif; font-weight: 500; color: var(--brand-blue);
    font-size: 14px; line-height: 17px;
  }
  .brand-mark__dot { width: 34px; height: 34px; border-radius: 50%; background: var(--brand-olive); margin-bottom: 8px; }
  .sheet--letter .brand-mark { left: 340px; top: 548px; width: 128px; height: 130px; }
  .sheet--fax .brand-mark { left: 320px; top: 542px; width: 134px; height: 138px; }

  .fax-title {
    position: absolute; left: 38px; top: 246px;
    font-family: "Roboto", sans-serif; font-size: 39px; color: var(--ink);
  }
  .fax-field {
    position: absolute; left: 42px; width: 415px; display: flex; align-items: flex-end;
    font-family: "Roboto", sans-serif; font-size: 10.5px; color: var(--ink-dark);
  }
  .fax-field__line { flex: 1; border-bottom: 1px solid var(--ink-dark); height: 10px; margin-left: 1px; }
  .f-from { top: 324px; } .f-to { top: 379px; } .f-phone { top: 435px; } .f-fax { top: 491px; }
</style>
</head>
<body>
  <h1 class="showcase-title">Letterhead + Fax Cover Sheet</h1>

  <section class="sheet sheet--letter">
    <header class="masthead">
      <div class="masthead__inner">
        <div class="masthead__name">Heron Staffing, LLC</div>
        <div class="masthead__address">412 Kestrel Ave. Suite 118 Mobile, AL 36619</div>
      </div>
    </header>

    <p class="letter-body salutation">Dear sir/Madam,</p>
    <p class="letter-body paragraph p1">Lorem ipsum dolor sit amet, an vel recteque dissentiet, detracto albucius platonem ex vel, eros repudiandae cu. Atqui aliquando nec an, unum graece adolescens vel ad. Id odio scae has, iudico euismod atomorum ius ea, cum ea honestatis quaerendum theophrastus. Mea honestatis quaerendum theophrastus. Mea</p>
    <p class="letter-body paragraph p2">Lorem ipsum dolor sit amet, an vel recteque dissentiet, detracto albucius platonem ex vel, eros repudiandae cu. Atqui aliquando nec an, unum graece adolescens vel ad. Id odio scae has, iudico euismod atomorum ius ea, cum ea honestatis quaerendum theophrastus. Mea doming repudiandae ex, cu cum civibus assentior posidonium. Quo etiam pertinax ex, te eros repudiandae cu. Atqui aliquando nec an, unum graece adolescens vel ad. Id odio scae honestatis quaerendum theophrastus. Mea</p>
    <p class="letter-body paragraph p3">Lorem ipsum dolor sit amet, an vel recteque dissentiet, detracto albucius platonem ex vel, eros repudiandae cu. Atqui aliquando nec an, unum graece adolescens vel ad. Id odio scae has, iudico euismod atomorum ius ea, cum ea honestatis quaerendum theophrastus. Mea honestatis quaerendum theophrastus. Mea</p>

    <p class="letter-body closing">Kind Regards</p>
    <p class="letter-body signer">Daniel Whitmore<span class="signer__role">Chief Alchemist</span></p>
    <div class="signature" role="img" aria-label="Handwritten signature"></div>

    <div class="brand-mark">
      <span class="brand-mark__dot"></span>
      <span>Heron Coastal<br>Workforce<br>Services</span>
    </div>
  </section>

  <section class="sheet sheet--fax">
    <header class="masthead">
      <div class="masthead__inner">
        <div class="masthead__name">Heron Staffing, LLC</div>
        <div class="masthead__address">412 Kestrel Ave. Suite 118 Mobile, AL 36619</div>
      </div>
    </header>

    <h2 class="fax-title">Fax</h2>
    <div class="fax-field f-from">From:<span class="fax-field__line"></span></div>
    <div class="fax-field f-to">To:<span class="fax-field__line"></span></div>
    <div class="fax-field f-phone">Phone:<span class="fax-field__line"></span></div>
    <div class="fax-field f-fax">Fax:<span class="fax-field__line"></span></div>

    <div class="brand-mark">
      <span class="brand-mark__dot"></span>
      <span>Heron Coastal<br>Workforce<br>Services</span>
    </div>
  </section>
</body>
</html>
```